Brindle Capital and Investments

Create a simple business card design using the logos attached. Make it similar but not exact to the reference photo. Brand guidelines are also included.

```html
<!DOCTYPE html>
<html lang="en">
<head>
<meta charset="utf-8">
<title>Brindle Capital and Investments — Business Card</title>
<link rel="stylesheet" href="https://fonts.googleapis.com/css2?family=Inter:wght@400;500;600&display=swap">
<style>
  :root {
    --backdrop: #ababab;
    --navy: #050a1f;
    --rust: #8a2a0c;
    --paper: #ffffff;
    --ink: #4a4a4a;
  }
  * { margin: 0; padding: 0; box-sizing: border-box; }
  html, body { width: 1200px; height: 1200px; overflow: hidden; }
  body {
    background: var(--backdrop);
    position: relative;
    font-family: "Inter", Arial, sans-serif;
  }
  .card {
    position: absolute;
    left: 405px;
    width: 432px;
    height: 252px;
  }
  .card-front {
    top: 282px;
    background: var(--navy);
    display: flex;
    align-items: center;
    justify-content: center;
  }
  .card-back {
    top: 593px;
    background: var(--paper);
  }
  .brand-name {
    font-family: "Inter", Arial, sans-serif;
    font-weight: 600;
    letter-spacing: 0.14em;
    text-transform: uppercase;
    display: flex;
    align-items: center;
    gap: 8px;
  }
  .brand-dot {
    width: 10px; height: 10px; border-radius: 50%;
    background: var(--rust);
    flex: none;
  }
  .card-front .brand-name { color: var(--paper); font-size: 17px; }
  .card-back .brand-name {
    position: absolute;
    left: 36px; top: 100px;
    color: var(--navy);
    font-size: 14px;
  }
  .person {
    position: absolute;
    left: 55px; top: 156px;
    color: var(--ink);
    font-size: 11.5px;
    line-height: 14px;
  }
  .person-name {
    color: var(--navy);
    font-weight: 600;
    font-size: 12px;
    text-transform: uppercase;
  }
  .person-credential { margin-top: 11px; }
  .contact {
    position: absolute;
    left: 245px; top: 157px;
    list-style: none;
    color: var(--ink);
    font-size: 11.5px;
    line-height: 14px;
  }
  .contact li { display: flex; align-items: flex-start; gap: 5px; }
  .contact-icon {
    flex: none;
    width: 10px; height: 10px; margin-top: 2px;
    border-radius: 50%;
    background: var(--rust);
    color: var(--paper);
    font-size: 8px; font-weight: 600;
    line-height: 10px; text-align: center;
  }
</style>
</head>
<body>
  <section class="card card-front">
    <div class="brand-name"><span class="brand-dot"></span>Brindle Capital</div>
  </section>

  <section class="card card-back">
    <div class="brand-name"><span class="brand-dot"></span>Brindle Capital</div>

    <div class="person">
      <p class="person-name">Dale R. Whitman</p>
      <p class="person-title">Managing Partner</p>
      <p class="person-credential">Board Certified, Commercial<br>Real Estate Law, State Board<br>of Legal Specialization</p>
    </div>

    <ul class="contact">
      <li><span class="contact-icon">e</span>dale@whitmanfirm.com</li>
      <li><span class="contact-icon">d</span>555.210.4482</li>
      <li><span class="contact-icon">c</span>555.210.4736</li>
      <li><span class="contact-icon">a</span>1480 Meadow Ridge Dr., Ste.400<br>Fairview, TX 75069</li>
    </ul>
  </section>
</body>
</html>
```